Corporate web site design for a blockchain oriented company

Design a web site for Kelvo Rix. The company works on blockchain projects, mostly in B2B . Logo and content of the web site are attached with the project.

Corporate web sites means that we need to present the company and, at least, two of its projects.

Target Market(s)

B2B (Telecom, Gvt, online e-commerce web sites, banks, insurance ...)

Number of Pages Required

3 page

Font styles to use
Sans Serif

Requirements
Must have
• Landing page
• Page for KYC product
• Page for Loyalty product
• Team presentation
• Contact form
• Company presentation
• Several section can be in one page.
Nice to have
• Teaser video per project.
Should not have
• Heavy web site with a lot of animations.

```html
<!DOCTYPE html>
<html lang="en">
<head>
<meta charset="utf-8">
<title>Kelvo Rix — Blockchain Solutions Provider</title>
<link rel="stylesheet" href="https://fonts.googleapis.com/css2?family=Michroma&family=Lato:wght@400;700;900&family=Open+Sans:wght@400;600;700&display=swap">
<style>
:root{
  --bg:#151515;
  --bg-deep:#0f0f10;
  --hero:#1a1b1f;
  --orange:#f26a12;
  --white:#ffffff;
  --text:#d6d6d6;
  --muted:#9a9a9a;
  --ghost:rgba(255,255,255,0.05);
  --ice:#bfe3f5;
  --card:#f2f2f2;
  --ink:#2a2a2a;
}
*{margin:0;padding:0;box-sizing:border-box}
html,body{width:1200px;height:3468px;overflow:hidden}
body{background:var(--bg);color:var(--text);font-family:'Open Sans',sans-serif;position:relative}
.abs{position:absolute}

/* Header */
.hero{left:0;top:0;width:1200px;height:605px;background:radial-gradient(ellipse at 50% 100%,#2a2d35 0%,var(--hero) 55%,#121316 100%)}
.brand{left:111px;top:22px;display:flex;align-items:center;gap:12px;font-family:'Michroma',sans-serif;font-size:26px;color:var(--white);letter-spacing:2px}
.brand-mark{width:22px;height:22px;border:2px solid var(--white)}
.nav{top:30px;left:530px;display:flex;font-family:'Open Sans',sans-serif;font-size:14px;color:var(--white)}
.nav a{color:var(--white);text-decoration:none;margin-right:34px;position:relative}
.nav a.active::before{content:"";position:absolute;left:-2px;right:-2px;top:-30px;height:4px;background:var(--orange)}
.hero-title{left:111px;top:196px;font-family:'Michroma',sans-serif;font-weight:400;font-size:43px;line-height:67px;color:var(--white);letter-spacing:1px}
.hero-title .accent{color:var(--orange)}
.hero-emblem{left:760px;top:130px;width:320px;height:320px;border-radius:50%;border:14px solid var(--ice);background:radial-gradient(circle,rgba(191,227,245,0.12),transparent 70%)}
.scroll-cue{left:588px;top:478px}

/* Section headings */
.ghost{width:1200px;left:0;text-align:center;font-family:'Lato',sans-serif;font-weight:900;font-size:92px;color:var(--ghost)}
.section-title{width:1200px;left:0;text-align:center;font-family:'Lato',sans-serif;font-weight:700;font-size:34px;color:var(--white)}

.about-text{left:190px;top:826px;width:820px;text-align:center;font-size:14.5px;line-height:29px;color:var(--text)}
.video{left:152px;top:936px;width:895px;height:389px;background:linear-gradient(120deg,#1d2a44 0%,#3b4f72 35%,#b06a3a 62%,#3a4760 100%)}
.play{left:572px;top:1102px;width:56px;height:56px;border-radius:50%;background:var(--orange);box-shadow:0 0 0 8px rgba(242,106,18,0.3)}
.play svg{position:absolute;left:21px;top:17px}

/* Products */
.product-img{top:1554px;width:435px;height:266px}
.loyalty-img{left:152px;background:linear-gradient(180deg,#081a3a 0%,#1d3f78 50%,#7a4a2a 100%)}
.kyc-img{left:613px;background:radial-gradient(ellipse at 55% 50%,#5a6a7a 0%,#1a2430 55%,#0a0d12 100%)}
.product-label{top:1834px;font-family:'Lato',sans-serif;font-size:21px;color:var(--white)}
.product-label span{font-family:'Open Sans',sans-serif;font-size:15px;color:var(--text);margin-left:8px}
.divider{left:598px;top:1906px}

/* Team */
.member{top:2132px;width:200px;text-align:center}
.avatar{width:134px;height:134px;border-radius:50%;margin:0 auto;border:4px solid var(--white);background:linear-gradient(180deg,#d9d4cc,#8a8580)}
.member-name{margin-top:12px;font-size:17px;color:var(--white)}
.member-role{font-size:12px;font-style:italic;color:var(--muted);margin-top:1px}
.member-social{display:flex;justify-content:center;gap:8px;margin-top:10px}
.member-social i{width:9px;height:9px;border-radius:50%;background:var(--white);display:block}

/* Blog */
.blog{left:152px;top:2451px;width:895px;height:481px;background:linear-gradient(135deg,#0c1e33 0%,#143454 50%,#0b1a2c 100%)}
.blog-title{left:152px;top:2515px;width:895px;text-align:center;font-family:'Lato',sans-serif;font-weight:700;font-size:34px;color:var(--white)}
.blog-tag{left:259px;top:2571px;width:136px;height:42px;background:var(--orange);color:var(--white);font-family:'Lato',sans-serif;font-weight:700;font-size:17px;line-height:42px;padding-left:30px}
.blog-card{left:259px;top:2613px;width:460px;height:198px;background:var(--card);padding:26px 36px;color:var(--ink);font-size:13.5px;font-weight:600;line-height:26px}
.blog-card a{display:inline-block;margin-top:6px;color:var(--orange);font-size:12px;font-weight:400;text-decoration:underline}

/* Footer */
.footer{left:0;top:3029px;width:1200px;height:439px;background:var(--bg-deep)}
.foot-col{top:3126px}
.foot-col h4{font-family:'Lato',sans-serif;font-weight:700;font-size:16px;color:var(--white);margin-bottom:32px;letter-spacing:.5px}
.foot-col li{list-style:none;font-size:12.5px;color:var(--text);height:32px}
.subscribe{left:765px;top:3186px;width:336px;height:44px;border-radius:22px;background:var(--white);font-size:12px;color:#8a8a8a;line-height:44px;padding-left:24px}
.subscribe span{position:absolute;right:0;top:0;width:95px;height:44px;border-radius:22px;background:var(--orange);color:var(--white);text-align:center;font-weight:700;font-size:13px}
.foot-social{left:765px;top:3292px;display:flex;gap:24px}
.foot-social i{display:block;width:14px;height:14px;border-radius:50%;background:var(--white)}
.copyright{left:0;top:3438px;width:1200px;text-align:center;font-size:12px;color:var(--muted)}
</style>
</head>
<body>

<header class="abs hero">
  <div class="abs brand"><span class="brand-mark"></span>Kelvo Rix</div>
  <nav class="abs nav">
    <a class="active">Home</a><a>About us</a><a>KYC Product</a><a>Loyalty Product</a><a>Team</a><a>Contact us</a>
  </nav>
  <h1 class="abs hero-title">BLOCKCHAIN<br><span class="accent">SOLUTIONS</span><br>PROVIDER</h1>
  <div class="abs hero-emblem"></div>
  <svg class="abs scroll-cue" width="24" height="50" viewBox="0 0 24 50" aria-hidden="true">
    <rect x="3" y="2" width="18" height="28" rx="9" fill="none" stroke="#fff" stroke-width="2"/>
    <line x1="12" y1="8" x2="12" y2="14" stroke="#fff" stroke-width="2"/>
    <path d="M7 40 L12 45 L17 40" fill="none" stroke="#fff" stroke-width="2"/>
  </svg>
</header>

<section>
  <div class="abs ghost" style="top:680px">About Us</div>
  <h2 class="abs section-title" style="top:750px">Welcome To Kelvo Rix</h2>
  <p class="abs about-text">Kelvo Rix Technology is a technology enabler that pledges to tackle issues that have plagued organisations for years. The company is lead by a team with tremendous expertise in the field of blockchain, mobile, IT, payment and financial sector. Being a global team, the company has influence in Singapore, China , France and more.</p>
  <div class="abs video" role="img" aria-label="Teaser video still: hand touching a glowing blockchain network of coin icons"></div>
  <div class="abs play"><svg width="18" height="22" viewBox="0 0 18 22" aria-hidden="true"><path d="M0 0 L18 11 L0 22Z" fill="#fff"/></svg></div>
</section>

<section>
  <div class="abs ghost" style="top:1396px">Products</div>
  <h2 class="abs section-title" style="top:1462px">Our Products</h2>
  <div class="abs product-img loyalty-img" role="img" aria-label="Night city skyline with connected network lights"></div>
  <div class="abs product-img kyc-img" role="img" aria-label="Hands holding a digital coin hologram"></div>
  <div class="abs product-label" style="left:152px">KR-LOYALTY :<span>Intuitive partnership solution</span></div>
  <div class="abs product-label" style="left:613px">KR-KYC :<span>Own your identity</span></div>
  <svg class="abs divider" width="4" height="64" viewBox="0 0 4 64" aria-hidden="true">
    <circle cx="2" cy="4" r="3.5" fill="#fff"/><line x1="2" y1="8" x2="2" y2="64" stroke="#fff" stroke-width="1"/>
  </svg>
</section>

<section>
  <div class="abs ghost" style="top:1988px">Our Team</div>
  <h2 class="abs section-title" style="top:2050px">Meet Our Team</h2>
  <div class="abs member" style="left:150px"><div class="avatar" role="img" aria-label="Portrait photo of team member"></div><div class="member-name">Mara Lind</div><div class="member-role">general manager</div><div class="member-social"><i></i><i></i><i></i></div></div>
  <div class="abs member" style="left:383px"><div class="avatar" role="img" aria-label="Portrait photo of team member"></div><div class="member-name">Mara Lind</div><div class="member-role">general manager</div><div class="member-social"><i></i><i></i><i></i></div></div>
  <div class="abs member" style="left:617px"><div class="avatar" role="img" aria-label="Portrait photo of team member"></div><div class="member-name">Mara Lind</div><div class="member-role">general manager</div><div class="member-social"><i></i><i></i><i></i></div></div>
  <div class="abs member" style="left:850px"><div class="avatar" role="img" aria-label="Portrait photo of team member"></div><div class="member-name">Mara Lind</div><div class="member-role">general manager</div><div class="member-social"><i></i><i></i><i></i></div></div>
</section>

<section>
  <div class="abs blog" role="img" aria-label="Blue circuit board world map background"></div>
  <h2 class="abs blog-title">BLOG</h2>
  <div class="abs blog-tag">Kelvo Rix</div>
  <article class="abs blog-card">With autonomous doors, car , drones and even delivery being very a real possibility (if not already) in the future, everything is sure becoming more and more accessible and Convenient.However, not all is sunshine and rainbow...<br><a>READ MORE</a></article>
</section>

<footer class="abs footer"></footer>
<div class="abs foot-col" style="left:99px"><h4>BUSINESS</h4><ul><li>Block Chain Projects</li><li>Services</li><li>Company</li><li>Blog</li></ul></div>
<div class="abs foot-col" style="left:335px"><h4>QUICK LINKS</h4><ul><li>Home</li><li>About us</li><li>KYC Product</li><li>Loyalty Product</li><li>Team</li><li>Contact us</li></ul></div>
<div class="abs foot-col" style="left:539px"><h4>LEGAL</h4><ul><li>Faq</li><li>Privacy Policy</li><li>Terms &amp; Conditions</li><li>Sitemap</li></ul></div>
<div class="abs foot-col" style="left:765px"><h4>SUBSCRIBE</h4></div>
<div class="abs subscribe">Enter Email Address<span>SEND</span></div>
<div class="abs foot-social"><i></i><i></i><i></i><i></i><i></i></div>
<div class="abs copyright">© 2019 by Kelvo Rix All Rights Reserved</div>

</body>
</html>
```